Copper lark buildworks

Copper lark buildworks is a small construction company.
Who is a licenced builder, Carpenter, joiner,
working on heritage ,new build, speacial projects and sometimes furniture

Industry/Entity Type

Construction

```html
<!DOCTYPE html>
<html lang="en">
<head>
<meta charset="utf-8">
<title>Copper lark buildworks – Business Card</title>
<link rel="stylesheet" href="https://fonts.googleapis.com/css2?family=Noto+Serif:wght@700&family=Questrial&display=swap">
<style>
  :root {
    --page-bg: #f2f2f2;
    --card-bg: #ffffff;
    --brand-green: #3a9a3c;
    --ink-dark: #1c1f22;
    --ink-soft: #3a3d40;
    --text-light: #ffffff;
  }
  * { box-sizing: border-box; margin: 0; padding: 0; }
  html, body {
    width: 1200px;
    height: 800px;
    overflow: hidden;
    background: var(--page-bg);
  }
  .canvas {
    position: relative;
    width: 1200px;
    height: 800px;
  }
  .business-card {
    position: absolute;
    left: 110px;
    top: 120px;
    width: 980px;
    height: 560px;
    background: var(--card-bg);
    box-shadow: 0 6px 24px rgba(0,0,0,0.12);
  }
  .brand {
    position: absolute;
    top: 110px;
    left: 0;
    width: 100%;
    display: flex;
    justify-content: center;
    align-items: center;
    gap: 14px;
  }
  .brand-mark {
    width: 26px;
    height: 26px;
    background: var(--brand-green);
  }
  .brand-name {
    font-family: "Noto Serif", Georgia, serif;
    font-weight: 700;
    font-size: 44px;
    color: var(--brand-green);
    letter-spacing: -0.5px;
  }
  .person {
    position: absolute;
    top: 232px;
    left: 0;
    width: 100%;
    text-align: center;
  }
  .person-name {
    font-family: "Noto Serif", Georgia, serif;
    font-weight: 700;
    font-size: 66px;
    line-height: 1;
    color: var(--brand-green);
    letter-spacing: -1px;
  }
  .person-title {
    margin-top: 10px;
    font-family: "Questrial", Arial, sans-serif;
    font-size: 19px;
    letter-spacing: 6px;
    color: var(--ink-dark);
    text-transform: uppercase;
  }
  .contact-row {
    position: absolute;
    top: 388px;
    left: 70px;
    right: 70px;
    display: flex;
    justify-content: space-between;
    align-items: center;
  }
  .contact-item {
    display: flex;
    align-items: center;
    gap: 14px;
    font-family: "Questrial", Arial, sans-serif;
    font-size: 20px;
    color: var(--ink-soft);
    letter-spacing: 0.5px;
  }
  .contact-icon {
    width: 34px;
    height: 34px;
    flex: none;
  }
  .footer-strip {
    position: absolute;
    top: 448px;
    left: 60px;
    right: 60px;
    height: 50px;
    display: flex;
    align-items: stretch;
    gap: 14px;
  }
  .stripe {
    width: 24px;
  }
  .stripe--green { background: var(--brand-green); }
  .stripe--dark { background: var(--ink-dark); }
  .tagline-bar {
    flex: 1;
    margin: 0 18px 0 10px;
    background: var(--brand-green);
    color: var(--text-light);
    font-family: "Questrial", Arial, sans-serif;
    font-size: 22px;
    letter-spacing: 0.5px;
    display: flex;
    align-items: center;
    justify-content: center;
  }
</style>
</head>
<body>
<main class="canvas">
  <section class="business-card">
    <div class="brand">
      <span class="brand-mark"></span>
      <span class="brand-name">Copper lark buildworks</span>
    </div>

    <div class="person">
      <h1 class="person-name">Rowan Hale</h1>
      <p class="person-title">President of Copper lark buildworks</p>
    </div>

    <div class="contact-row">
      <div class="contact-item">
        <svg class="contact-icon" viewBox="0 0 34 34" aria-hidden="true">
          <circle cx="17" cy="17" r="17" fill="var(--ink-dark)"/>
          <path d="M12.2 9.5c.6-.4 1.4-.3 1.8.3l1.6 2.4c.4.6.3 1.3-.2 1.8l-1 .9c.8 1.8 2.2 3.3 4 4.1l.9-1c.5-.5 1.2-.6 1.8-.2l2.4 1.6c.6.4.7 1.2.3 1.8l-.9 1.3c-.6.8-1.6 1.2-2.6.9-4.4-1.3-7.8-4.7-9.1-9.1-.3-1 .1-2 .9-2.6z" fill="#fff"/>
        </svg>
        <span>0431207559</span>
      </div>
      <div class="contact-item">
        <svg class="contact-icon" viewBox="0 0 34 34" aria-hidden="true">
          <circle cx="17" cy="17" r="17" fill="var(--ink-dark)"/>
          <rect x="9" y="11.5" width="16" height="11" rx="1" fill="#fff"/>
          <path d="M9.5 12.2 17 18l7.5-5.8" fill="none" stroke="var(--ink-dark)" stroke-width="1.4"/>
        </svg>
        <span>info@copperlark.com</span>
      </div>
      <div class="contact-item">
        <svg class="contact-icon" viewBox="0 0 34 34" aria-hidden="true">
          <circle cx="17" cy="17" r="17" fill="var(--ink-dark)"/>
          <text x="17" y="20" text-anchor="middle" font-family="Arial, sans-serif" font-size="8" fill="#fff">www</text>
        </svg>
        <span>www.copperlark.com</span>
      </div>
    </div>

    <div class="footer-strip">
      <span class="stripe stripe--green"></span>
      <span class="stripe stripe--dark"></span>
      <div class="tagline-bar">Morbi orci quam, pulvinar dignissim</div>
      <span class="stripe stripe--dark"></span>
      <span class="stripe stripe--green"></span>
    </div>
  </section>
</main>
</body>
</html>
```